Sandwich Board and Poster design promoting a medical aesthetic clinic

I am looking for a clean, modern and relaxing design promoting a medical physician-led aesthetic clinic.
Services offered are neuromodulator treatment (Quelvo) and Dermal Fillers.
Logo must be included.
Use the tag line "Refresh your look, revive your spirit."
Address is 204-205 27361 92 Ave, Surrey, V7K 2M4
604-555-0148
email - info@lumawellpine.ca
www.lumawellpine.ca

```html
<!DOCTYPE html>
<html lang="en">
<head>
<meta charset="UTF-8">
<title>Lumawell Pine – Poster</title>
<link rel="stylesheet" href="https://fonts.googleapis.com/css2?family=PT+Sans:wght@400;700&family=Montserrat:wght@500;700&display=swap">
<style>
  :root {
    --backdrop: #ece4de;
    --paper: #f2f0ea;
    --ink: #1f3a45;
    --gold: #b8912f;
    --mist-soft: rgba(190, 205, 203, 0.55);
    --icon-disc: #c5d1cf;
  }
  * { margin: 0; padding: 0; box-sizing: border-box; }
  html, body { width: 1200px; height: 800px; overflow: hidden; }
  body {
    background: var(--backdrop);
    font-family: "PT Sans", Arial, sans-serif;
    color: var(--ink);
    position: relative;
  }
  .poster {
    position: absolute;
    left: 350px; top: 25px;
    width: 500px; height: 750px;
    background: var(--paper);
    overflow: hidden;
    box-shadow: 0 2px 10px rgba(0,0,0,0.08);
  }
  .wash {
    position: absolute;
    background: var(--mist-soft);
    border-radius: 46% 54% 40% 60% / 55% 45% 55% 45%;
    filter: blur(3px);
  }
  .wash--top-right { right: -10px; top: -8px; width: 130px; height: 30px; }
  .wash--right { right: -20px; top: 95px; width: 70px; height: 270px; }
  .wash--left { left: -18px; top: 88px; width: 70px; height: 70px; }
  .wash--lower-left { left: -25px; top: 500px; width: 110px; height: 200px; }
  .wash--bottom { left: 200px; bottom: -20px; width: 160px; height: 90px; }

  .brand {
    position: absolute;
    left: 24px; top: 72px;
    font-family: "Montserrat", Arial, sans-serif;
    font-weight: 500;
    font-size: 12px;
    letter-spacing: 2.5px;
    white-space: nowrap;
    color: var(--ink);
  }

  .hero-photo {
    position: absolute;
    left: 0; top: 128px;
    width: 418px; height: 268px;
    border-radius: 4px 30px 12px 4px;
    background: linear-gradient(120deg, #4a5fb0 0%, #5a6fbf 28%, #9b6a52 50%, #7a4c38 70%, #2b2b2e 100%);
  }
  .line-art {
    position: absolute;
    left: 0; top: 400px;
    width: 160px; height: 190px;
    background: radial-gradient(ellipse at center, rgba(184,145,47,0.10), rgba(184,145,47,0) 70%);
  }

  .tagline {
    position: absolute;
    left: 176px; top: 420px;
    font-size: 35px;
    font-weight: 400;
    line-height: 1.08;
    color: var(--ink);
  }
  .services {
    position: absolute;
    left: 178px; top: 506px;
    font-size: 12px;
    letter-spacing: 1px;
    color: var(--gold);
  }
  .contact {
    position: absolute;
    left: 182px;
    display: flex; align-items: center; gap: 12px;
  }
  .contact--address { top: 536px; }
  .contact--phone { top: 578px; }
  .contact__icon {
    width: 28px; height: 28px;
    border-radius: 50%;
    background: var(--icon-disc);
    display: flex; align-items: center; justify-content: center;
    flex-shrink: 0;
  }
  .contact__text { font-size: 13.5px; color: var(--ink); }
  .contact__label {
    font-family: "Montserrat", Arial, sans-serif;
    font-weight: 700;
    font-size: 11px;
    letter-spacing: 0.3px;
    display: block;
    margin-bottom: 2px;
  }
  .footer-line {
    position: absolute;
    bottom: 46px;
    font-size: 9.5px;
    color: var(--ink);
  }
  .footer-line--email { left: 23px; }
  .footer-line--web { right: 38px; }
</style>
</head>
<body>
  <main class="poster">
    <div class="wash wash--top-right"></div>
    <div class="wash wash--right"></div>
    <div class="wash wash--left"></div>
    <div class="wash wash--lower-left"></div>
    <div class="wash wash--bottom"></div>

    <header class="brand">LUMAWELL PINE</header>

    <div class="hero-photo" role="img" aria-label="Photo of a gloved practitioner giving a brow injection to a relaxed client with closed eyes"></div>
    <div class="line-art" role="img" aria-label="Fine gold line drawing of a woman's profile with flowing hair"></div>

    <h1 class="tagline">Refresh your look,<br>revive your spirit</h1>
    <p class="services">Quelvo · Dermal Fillers</p>

    <div class="contact contact--address">
      <span class="contact__icon">
        <svg width="12" height="16" viewBox="0 0 12 16"><path d="M6 0C2.7 0 0 2.6 0 5.9 0 10.3 6 16 6 16s6-5.7 6-10.1C12 2.6 9.3 0 6 0zm0 8.2A2.3 2.3 0 1 1 6 3.6a2.3 2.3 0 0 1 0 4.6z" fill="#b8912f"/></svg>
      </span>
      <span class="contact__text">204-205 27361 92 Ave, Surrey, V7K 2M4</span>
    </div>

    <div class="contact contact--phone">
      <span class="contact__icon">
        <svg width="15" height="15" viewBox="0 0 24 24"><path d="M6.6 10.8a15.1 15.1 0 0 0 6.6 6.6l2.2-2.2c.3-.3.7-.4 1-.2 1.1.4 2.3.6 3.6.6.6 0 1 .4 1 1V20c0 .6-.4 1-1 1A17 17 0 0 1 3 4c0-.6.4-1 1-1h3.5c.6 0 1 .4 1 1 0 1.3.2 2.5.6 3.6.1.3 0 .7-.2 1z" fill="#b8912f"/></svg>
      </span>
      <span class="contact__text"><span class="contact__label">CONTACT US</span>604-555-0148</span>
    </div>

    <p class="footer-line footer-line--email">Email: info@lumawellpine.ca</p>
    <p class="footer-line footer-line--web">Visit: www.lumawellpine.ca</p>
  </main>
</body>
</html>
```